Catering company needs business cards

We need new business cards for growing catering company.

Industry/Entity Type

Business

Requirements
Must have
• Company logo
• Marisol Ventrella
• Catering Director
• marisol.t.ventrella-1@orbixal.com
• 407-552-1748
• 407-663-2917
• Building R3-718 PQT
• Halvorsen Launch Complex
• Florida, 32741

```html
<!DOCTYPE html>
<html lang="en">
<head>
<meta charset="utf-8">
<title>The Open Air Catering Company – Business Card</title>
<link href="https://fonts.googleapis.com/css2?family=Open+Sans:wght@400;600;700&display=swap" rel="stylesheet">
<style>
  :root {
    --stage: #141414;
    --card-white: #ffffff;
    --brand-blue: #2f7fc6;
    --ink: #2b2b2b;
    --sky-deep: #2f7bc8;
    --sky-mid: #6aa8e0;
    --sky-light: #d6e8f7;
    --cloud: #f4f8fc;
  }
  * { box-sizing: border-box; margin: 0; padding: 0; }
  html, body { width: 1200px; height: 1130px; overflow: hidden; }
  body {
    background: var(--stage);
    font-family: "Open Sans", Arial, sans-serif;
    position: relative;
  }
  .card {
    position: absolute;
    left: 180px;
    width: 840px;
    height: 480px;
    overflow: hidden;
  }
  .card--info { top: 60px; background: var(--card-white); }
  .card--cover { top: 590px; }

  .sky-strip {
    position: absolute;
    top: 0;
    height: 100%;
    background: linear-gradient(170deg, var(--cloud) 0%, var(--sky-mid) 35%, var(--sky-light) 60%, var(--sky-deep) 100%);
  }
  .sky-strip--left { left: 0; width: 66px; }
  .sky-strip--right { right: 0; width: 84px; }

  .sky-photo {
    position: absolute;
    inset: 0;
    background:
      radial-gradient(ellipse at 20% 20%, rgba(255,255,255,.85), transparent 40%),
      radial-gradient(ellipse at 80% 55%, rgba(255,255,255,.7), transparent 35%),
      radial-gradient(ellipse at 35% 85%, rgba(255,255,255,.75), transparent 38%),
      linear-gradient(160deg, var(--sky-mid), var(--sky-deep) 55%, var(--sky-mid));
  }

  .company-name {
    position: absolute;
    left: 0; right: 0;
    display: flex;
    align-items: center;
    justify-content: center;
    gap: 14px;
    font-weight: 600;
    white-space: nowrap;
  }
  .company-name__dot { border-radius: 50%; flex: none; }

  .card--info .company-name { top: 62px; color: var(--brand-blue); font-size: 30px; }
  .card--info .company-name__dot { width: 14px; height: 14px; background: var(--brand-blue); }

  .card--cover .company-name { top: 200px; color: #fff; font-size: 40px; }
  .card--cover .company-name__dot { width: 18px; height: 18px; background: #fff; }

  .holder { position: absolute; top: 196px; left: 0; right: 0; text-align: center; }
  .holder__name { color: var(--brand-blue); font-weight: 700; font-size: 19px; text-transform: uppercase; }
  .holder__title { color: var(--ink); font-size: 18px; font-weight: 600; }

  .contact {
    position: absolute;
    left: 130px;
    right: 120px;
    top: 318px;
    color: var(--ink);
    font-size: 16px;
    line-height: 1.45;
  }
  .contact__address { text-align: center; margin-bottom: 8px; }
  .contact__grid { display: grid; grid-template-columns: 18px auto 18px auto; column-gap: 10px; }
  .contact__label { color: var(--brand-blue); font-weight: 700; }
</style>
</head>
<body>
  <section class="card card--info">
    <div class="sky-strip sky-strip--left" role="img" aria-label="Blue sky with white clouds photograph"></div>
    <div class="sky-strip sky-strip--right" role="img" aria-label="Blue sky with white clouds photograph"></div>

    <div class="company-name">
      <span class="company-name__dot"></span>
      <span>The Open Air Catering Company</span>
    </div>

    <div class="holder">
      <div class="holder__name">Marisol Ventrella</div>
      <div class="holder__title">Catering Director</div>
    </div>

    <div class="contact">
      <p class="contact__address">Building R3-718 PQT, Halvorsen Launch Complex, Florida, 32741</p>
      <div class="contact__grid">
        <span class="contact__label">T</span><span>407-552-1748</span>
        <span class="contact__label">F</span><span>407-663-2917</span>
        <span class="contact__label">E</span><span>marisol.t.ventrella-1@orbixal.com</span>
        <span class="contact__label">W</span><span>openaircatering.com</span>
      </div>
    </div>
  </section>

  <section class="card card--cover">
    <div class="sky-photo" role="img" aria-label="Blue sky with clouds blended over a table setting with cutlery and a wine glass"></div>
    <div class="company-name">
      <span class="company-name__dot"></span>
      <span>The Open Air Catering Company</span>
    </div>
  </section>
</body>
</html>
```